New Podcast focussing on non-mainstream interventions for guidance needs podcast art

I need an exquisite piece of podcast art work for the launch of my new podcast 'Past the Hollow'. This podcast explores unorthodox, esoteric and unconventional methods to find peace, clarity and direction in life. Topics include family Constellations Systems, Psychedelics, Equine Therapy and Floatation to name a few. A teaser has been posted on Brevlo with a strong response. The audience is primarily midlifers or those in a career/personal crisis of direction. It's meant to comfort, inform and empower and offer other ways rather than mainstream to work out what to do with your life. The file shared with you shows the pic used on Brevlo as it's illustrating the idea of illumination. You can use it or not, and whilst I am ex-Military, I don't want the cover to convey an overly military influence. I'd like 'Past the Hollow' to feature on the art work and my name, Margot Pennick. I'd like inspiration, creativity, and the idea of hope conveyed as well as clarity and courage. Whilst the podcast is about finding your direction please do no use compass images or cross road images as that is too obvious.
Hope that all helps. Looking forward to your ideas.

```html
<!DOCTYPE html>
<html lang="en">
<head>
<meta charset="utf-8">
<title>Past the Hollow — Podcast Cover</title>
<link rel="stylesheet" href="https://fonts.googleapis.com/css2?family=Montserrat:wght@500;800&family=Crimson+Text:wght@400&display=swap">
<style>
  :root {
    --stage: #e6e6e6;
    --gold: #d8bf66;
    --gold-deep: #a8883a;
    --crimson: #9a1a1d;
    --ink-dark: #140906;
    --ember: #4a2410;
    --cream: #f4ecdc;
    --white: #ffffff;
  }
  * { box-sizing: border-box; margin: 0; padding: 0; }
  html, body {
    width: 1200px;
    height: 940px;
    overflow: hidden;
    background: var(--stage);
  }
  .cover {
    position: absolute;
    left: 160px;
    top: 30px;
    width: 880px;
    height: 880px;
    overflow: hidden;
    background: var(--ink-dark);
  }
  .cover-photo {
    position: absolute;
    inset: 0;
    background:
      radial-gradient(circle at 45% 33%, #fffbe2 0, #f7cb45 3%, #d1901f 11%, rgba(120, 64, 16, 0.85) 24%, rgba(60, 30, 10, 0) 44%),
      radial-gradient(ellipse at 75% 60%, rgba(12, 6, 4, 0.8) 0, rgba(12, 6, 4, 0) 55%),
      linear-gradient(180deg, #1a0c08 0%, #2e170b 40%, #54301a 62%, var(--ember) 74%, #1c0d07 100%);
  }
  .cover-art {
    position: absolute;
    inset: 0;
    width: 100%;
    height: 100%;
  }
  .show-title {
    position: absolute;
    left: 40px;
    top: 40px;
    display: flex;
    flex-direction: column;
    align-items: flex-end;
    font-family: "Montserrat", sans-serif;
    font-weight: 800;
    color: var(--gold);
    line-height: 0.88;
    letter-spacing: -0.035em;
  }
  .show-title .big { font-size: 74px; }
  .show-title .row { display: flex; align-items: flex-start; }
  .show-title .small {
    font-size: 27px;
    letter-spacing: -0.01em;
    margin-top: 6px;
    margin-right: 3px;
  }
  .topics {
    position: absolute;
    right: 43px;
    top: 40px;
    font-family: "Montserrat", sans-serif;
    font-weight: 500;
    font-size: 12px;
    line-height: 1.2;
    color: var(--white);
    white-space: nowrap;
  }
  .host-name {
    position: absolute;
    left: 40px;
    top: 790px;
    font-family: "Crimson Text", serif;
    font-size: 50px;
    line-height: 1;
    color: var(--cream);
    letter-spacing: -0.01em;
    white-space: nowrap;
  }
</style>
</head>
<body>
  <section class="cover">
    <div class="cover-photo" role="img" aria-label="Photograph of a figure at dusk before a sunburst over hills and trees"></div>

    <svg class="cover-art" viewBox="0 0 1262 1262" aria-hidden="true">
      <line class="frame-line" x1="61" y1="277" x2="61" y2="1119" stroke="var(--gold)" stroke-width="2"/>
      <line class="frame-line" x1="1200" y1="95" x2="1200" y2="930" stroke="var(--gold)" stroke-width="2"/>
      <line class="name-rule" x1="515" y1="1200" x2="900" y2="1200" stroke="var(--gold)" stroke-width="2"/>
      <path class="corner-sweep" d="M650 1262 C960 1200 1205 1040 1262 820 L1262 1262 Z" fill="var(--crimson)"/>
      <path class="corner-edge" d="M650 1262 C960 1200 1205 1040 1262 820" fill="none" stroke="var(--gold-deep)" stroke-width="6"/>
      <g class="mic-icon" fill="none" stroke="var(--gold)" stroke-width="9" stroke-linecap="round">
        <rect x="1126" y="1062" width="58" height="104" rx="29"/>
        <line x1="1140" y1="1092" x2="1170" y2="1092"/>
        <line x1="1140" y1="1112" x2="1170" y2="1112"/>
        <line x1="1140" y1="1132" x2="1170" y2="1132"/>
        <path d="M1108 1130 C1108 1200 1202 1200 1202 1130"/>
        <line x1="1155" y1="1182" x2="1155" y2="1204"/>
        <line x1="1135" y1="1204" x2="1175" y2="1204"/>
      </g>
    </svg>

    <h1 class="show-title">
      <span class="big">Past</span>
      <span class="row"><span class="small">THE</span><span class="big">Hollow</span></span>
    </h1>
    <p class="topics">Family Constellations Systems | Psychedelics | Equine Therapy | Floatation</p>
    <p class="host-name">Margot Pennick</p>
  </section>
</body>
</html>
```